Square Business Cards for Our Restaurant / Event Venue

We need square business cards designed for the management team of our event venue and restaurant. On one side of the card should be the the Harbor Lantern 7 logo and URL www.harborlantern7.example. On the other side should be the Ember Logo and URL www.emberhall7.example. All employee details should be on the side with Ember logo. There will be a total of 5 cards to be created with the design.

Clara Bennquist
clara@harborlantern7.example

main 555.418.3072
direct 555.730.2946

4831 West Orchard Lane SE
Washington, DC 90417

Industry/Entity Type

Business

```html
<!DOCTYPE html>
<html lang="en">
<head>
<meta charset="utf-8">
<title>Ember – Clara Bennquist</title>
<link rel="stylesheet" href="https://fonts.googleapis.com/css2?family=Didact+Gothic&display=swap">
<style>
  :root {
    --backdrop: #e6ddcf;
    --card: #ffffff;
    --ink: #1c1c1c;
    --ink-soft: #3a3a3a;
    --accent: #c8272d;
    --shadow: rgba(60, 45, 25, 0.18);
  }
  * { margin: 0; padding: 0; box-sizing: border-box; }
  html, body {
    width: 1200px;
    height: 813px;
    overflow: hidden;
    background: var(--backdrop);
  }
  body {
    position: relative;
    font-family: "Didact Gothic", "Century Gothic", sans-serif;
    color: var(--ink);
  }
  .business-card {
    position: absolute;
    left: 280px;
    top: 86px;
    width: 640px;
    height: 640px;
    background: var(--card);
    box-shadow: 0 6px 22px var(--shadow);
  }
  .brand {
    position: absolute;
    left: 0;
    right: 0;
    top: 62px;
    text-align: center;
  }
  .brand-name {
    font-size: 84px;
    line-height: 1;
    color: var(--ink);
    letter-spacing: 1px;
  }
  .rule {
    position: absolute;
    left: 109px;
    width: 413px;
    height: 4px;
    background: var(--accent);
  }
  .rule--top { top: 216px; }
  .rule--bottom { top: 530px; }
  .person-name {
    position: absolute;
    left: 0;
    right: 0;
    top: 236px;
    text-align: center;
    font-size: 25px;
    color: var(--ink-soft);
  }
  .phone-list {
    position: absolute;
    left: 197px;
    top: 305px;
    list-style: none;
  }
  .phone-line {
    display: flex;
    align-items: center;
    height: 54px;
    font-size: 29px;
    color: var(--ink-soft);
  }
  .phone-icon {
    width: 38px;
    height: 40px;
    margin-right: 16px;
    fill: var(--ink);
  }
  .address {
    position: absolute;
    left: 0;
    right: 0;
    top: 446px;
    text-align: center;
    font-style: normal;
    font-size: 22px;
    line-height: 33px;
    color: var(--ink-soft);
  }
  .email {
    position: absolute;
    left: 0;
    right: 0;
    top: 557px;
    text-align: center;
    font-size: 22px;
    color: var(--ink-soft);
  }
  .website {
    position: absolute;
    left: 0;
    right: 0;
    top: 596px;
    text-align: center;
    font-size: 18px;
    color: var(--accent);
  }
</style>
</head>
<body>
  <article class="business-card">
    <header class="brand">
      <span class="brand-name">Ember</span>
    </header>

    <div class="rule rule--top"></div>

    <p class="person-name">Clara Bennquist</p>

    <ul class="phone-list">
      <li class="phone-line">
        <svg class="phone-icon" viewBox="0 0 38 40" aria-label="Main line">
          <path d="M3 13 C3 6 10 4 19 4 C28 4 35 6 35 13 L35 15 L27 15 L26 11 C22 10 16 10 12 11 L11 15 L3 15 Z"/>
          <path d="M9 17 L29 17 L34 36 L4 36 Z"/>
          <circle cx="19" cy="26" r="5" fill="#ffffff"/>
          <circle cx="19" cy="26" r="2.4"/>
        </svg>
        <span>555.418.3072</span>
      </li>
      <li class="phone-line">
        <svg class="phone-icon" viewBox="0 0 38 40" aria-label="Direct line">
          <rect x="8" y="1" width="22" height="38" rx="4"/>
          <rect x="11" y="6" width="16" height="25" fill="#ffffff"/>
          <circle cx="19" cy="35" r="1.8" fill="#ffffff"/>
        </svg>
        <span>555.730.2946</span>
      </li>
    </ul>

    <address class="address">
      4831 West Orchard Lane SE<br>
      Washington, DC 90417
    </address>

    <div class="rule rule--bottom"></div>

    <p class="email">clara@harborlantern7.example</p>
    <p class="website">www.emberhall7.example</p>
  </article>
</body>
</html>
```